Verpackungsdesign (Beutel) für Mentholkristalle
Zielgruppe
Wir sind im eCommerce tätig und verkaufen somit ausschließlich online. Zielgruppe für dieses Produkt sind Saunagänger.
Aufgabenstellung
Es handelt sich um ein Design für einen Beutel. Das Produkt sind Mentholkristalle.
Es handelt sich um die Marke Mokal - wobei dies nicht unbedingt so präsent sein muss. Es gibt kein Logo - es kann allerdings für eine bessere Optik für die Vorderseite ein Logo erstellt werden.
Die Maße des Beutels sind in etwa 130x200mm. Eine Stanzform ist beigefügt.
Dieser Stil gefällt mir gut: https://www.kaufhafen.de/dp/Q739LMXPZ4/
Derzeitiges Design: https://www.kaufhafen.de/dp/Q5182RNKJT
Benötigt werden am Ende die Rohdaten (PSD, AI Dateien etc.) sowie sämtlichen Rechte alles kommerziell benutzen sowie verändern zu dürfen.
Ein Briefing ist im Anhang beigefügt.

```html
<!DOCTYPE html>
<html lang="de">
<head>
<meta charset="utf-8">
<title>Mokal Mentholkristalle – Beutel Vorder- und Rückseite</title>
<link href="https://fonts.googleapis.com/css2?family=Bebas+Neue&family=Caveat:wght@500&family=Open+Sans:wght@400;700&display=swap" rel="stylesheet">
<style>
  :root {
    --stage: #eef0ee;
    --paper: #ffffff;
    --tile-teal: #96cdd3;
    --navy: #0f3b63;
    --soft-teal: #6bbcc4;
    --ean-pink: #ea8fbe;
    --ink: #1f2a33;
  }
  * { margin: 0; padding: 0; box-sizing: border-box; }
  html, body { width: 1200px; height: 1200px; overflow: hidden; background: var(--stage); }
  .stage { position: relative; width: 1200px; height: 1200px; }

  .pouch-face {
    position: absolute; top: 215px; width: 500px; height: 770px;
    background: var(--paper);
    box-shadow: 6px 8px 14px rgba(0,0,0,0.18);
    overflow: hidden;
    font-family: "Open Sans", sans-serif; color: var(--ink);
  }
  .pouch-face--front { left: 80px; }
  .pouch-face--back { left: 620px; }

  .tile-pattern { position: absolute; left: 0; top: 0; display: block; }

  /* Front */
  .brand-window {
    position: absolute; left: 167px; top: 166px; width: 166px; height: 111px;
    background: var(--paper);
    display: flex; align-items: center; justify-content: center; gap: 8px;
  }
  .brand-window__dot { width: 10px; height: 10px; border-radius: 50%; background: var(--tile-teal); }
  .brand-window__name {
    font-family: "Bebas Neue", sans-serif; font-size: 34px; letter-spacing: 3px; color: var(--tile-teal);
  }
  .claim-script {
    position: absolute; left: 0; width: 100%; top: 482px; text-align: center;
    font-family: "Caveat", cursive; font-size: 30px; color: var(--navy); letter-spacing: 1px;
  }
  .product-title {
    position: absolute; left: 0; width: 100%; top: 532px; text-align: center;
    font-family: "Bebas Neue", sans-serif; font-size: 50px; letter-spacing: 3px; color: var(--navy); line-height: 1;
  }
  .product-subtitle {
    position: absolute; left: 0; width: 100%; top: 594px; text-align: center;
    font-family: "Bebas Neue", sans-serif; font-size: 30px; letter-spacing: 2px; color: var(--soft-teal); line-height: 1;
  }
  .recycling-badge { position: absolute; left: 72px; top: 678px; width: 56px; height: 46px; background: var(--navy); }
  .net-weight {
    position: absolute; right: 58px; top: 696px;
    font-family: "Bebas Neue", sans-serif; font-size: 30px; letter-spacing: 2px; color: var(--navy); line-height: 1;
  }

  /* Back */
  .info-heading {
    position: absolute; left: 0; width: 100%; text-align: center;
    font-family: "Bebas Neue", sans-serif; font-size: 19px; letter-spacing: 1px; color: var(--navy); line-height: 1;
  }
  .info-text {
    position: absolute; left: 72px; width: 356px; text-align: center;
    font-size: 9px; line-height: 1.45;
  }
  .info-text--intro { left: 80px; width: 340px; top: 181px; }
  .usage-columns {
    position: absolute; left: 38px; top: 388px; width: 426px;
    display: grid; grid-template-columns: repeat(3, 1fr); gap: 14px;
  }
  .usage-option__title {
    font-size: 8px; font-weight: 700; text-transform: uppercase; text-align: center;
    line-height: 1.3; height: 26px; color: var(--ink);
  }
  .usage-option__text { font-size: 9px; line-height: 1.5; text-align: justify; text-align-last: center; }
  .safety-text { left: 40px; width: 420px; top: 603px; }
  .imprint {
    position: absolute; left: 43px; top: 660px; font-size: 7.5px; line-height: 1.4; font-weight: 700; font-style: normal;
  }
  .ean-space {
    position: absolute; left: 312px; top: 674px; width: 140px; height: 51px;
    background: var(--ean-pink); color: var(--navy);
    font-family: "Bebas Neue", sans-serif; font-size: 18px; letter-spacing: 1px; line-height: 1;
    display: flex; flex-direction: column; align-items: center; justify-content: center;
  }
</style>
</head>
<body>
<main class="stage">

  <section class="pouch-face pouch-face--front" aria-label="Vorderseite">
    <svg class="tile-pattern" width="500" height="444" viewBox="0 0 500 444" role="img" aria-label="Geometrisches Kachelmuster mit Blatt- und Kreismotiven in Türkis">
      <rect width="500" height="444" fill="var(--tile-teal)"/>
    </svg>
    <div class="brand-window">
      <span class="brand-window__dot"></span>
      <span class="brand-window__name">Mokal</span>
    </div>
    <p class="claim-script">100% natürlich</p>
    <h1 class="product-title">Mentholkristalle</h1>
    <p class="product-subtitle">Ideal für die Sauna</p>
    <div class="recycling-badge" aria-hidden="true"></div>
    <p class="net-weight">100 G</p>
  </section>

  <section class="pouch-face pouch-face--back" aria-label="Rückseite">
    <svg class="tile-pattern" width="500" height="219" viewBox="0 0 500 219" role="img" aria-label="Geometrisches Kachelmuster mit Blatt- und Kreismotiven in Türkis">
      <path d="M0 0 H500 V219 H446 V109 H52 V219 H0 Z" fill="var(--tile-teal)"/>
    </svg>

    <h2 class="info-heading" style="top:156px">Mentholkristalle</h2>
    <p class="info-text info-text--intro">Unsere Mentholkristalle bestehen aus 100 % reinem Minzöl, welches sorgfältig und unter hohen Standards, von einer unserer Partnerfarmen in Indien, aus den frisch geernteten Minzblättern, gewonnen wird – daher erhalten Sie die Mentholkristalle in pharmazeutischer Qualität.</p>

    <h2 class="info-heading" style="top:266px">Lagerung &amp; Dosierung</h2>
    <p class="info-text" style="top:292px">Verwenden Sie je nach Größe der Kabine und größe der Kristalle 1–3 Stück (ca. 2 g) bei einem Saunagang. Kühl und trocken lagern und Verpackung bitte nicht in die Sauna mitnehmen – Schmelzgefahr!</p>

    <h2 class="info-heading" style="top:360px">Anwendungshinweise - 3 Optionen</h2>
    <div class="usage-columns">
      <div class="usage-option">
        <p class="usage-option__title">Direkt auf<br>die Steine</p>
        <p class="usage-option__text">Legen Sie vorsichtig die Kristalle auf einen großen Saunastein. Sorgen Sie zuvor dafür, dass die Steine nicht zu heiß sind (vorher mit Wasser abkühlen), da das reine Öl entflammen könnte. Das Öl der Kristalle darf nicht auf die Heizstäbe gelangen.</p>
      </div>
      <div class="usage-option">
        <p class="usage-option__title">Traditionell in<br>Wasser auflösen</p>
        <p class="usage-option__text">Lösen Sie die Kristalle vorher in einem Aufgusseimer mit warmen Wasser auf. Danach können Sie einen traditionellen Saunaaufguss mit mehreren Aufgussrunden zelebrieren.</p>
      </div>
      <div class="usage-option">
        <p class="usage-option__title">In der Kelle<br>schmelzen lassen</p>
        <p class="usage-option__text">Geben Sie die Kristalle lediglich bei der ersten Aufgussrunde, gemischt mit Wasser, in die Saunakelle und gießen Sie diese vorsichtig über die Saunasteine. Bei den restlichen Aufgussrunden können Sie einen Duft Ihrer Wahl nehmen.</p>
      </div>
    </div>

    <h2 class="info-heading" style="top:577px">Sicherheitshinweise</h2>
    <p class="info-text safety-text">Reizt die Haut – Nicht in die Augen oder auf die Schleimhäute bringen – Für Kinder unzugänglich aufbewahren – Nicht in die Saunakabine mitnehmen – Sparsam dosieren!</p>

    <address class="imprint">
      Made in India<br>
      Mokal eine Marke der<br>
      Vendura GmbH<br>
      Lindenweg 14<br>
      D-60311 Frankfurt a.M.<br>
      www.vendura-handel.de<br>
      info@vendura-handel.de
    </address>
    <div class="ean-space"><span>Platz für</span><span>EAN-Code</span></div>
  </section>

</main>
</body>
</html>
```